Business Card Design

RETAIL HIGH END CONTEMPORARY WOMEN'S CLOTHING STORE
MODERN, SIMPLE, CLEAN, COOL

WE ARE ALL ABOUT NY and CALIF STYLE.... CLASSY but EDGY..
COOLEST DENIM , Trendsetting, NEUTRAL Pallettes,
Collections : Fig and Stone, Dorian Vesk, PMW, K47, QTB
Don't need names of collections on card. thats just good info
for designer of card.

WOULD LIKE THE FONT TO BE INTERESTING, but CLEAN
We are on facebook daily with photos of outfits we put together
which you can look up and friend us.... MolvaHarbor
Also on instagram .
Open to options on color and size, but need cool and fresh.

Contact Information for Business Card

DELLA 5417 Larkmoor Rd. #309 Ember Court Arcade..Va. Beach, Va. 23987
Phone 757.386.5049 Fax 757.386-2613 EMAIL..DELLAMODE@QUILLBOX.COM

```html
<!DOCTYPE html>
<html lang="en">
<head>
<meta charset="utf-8">
<title>DELLA – Business Card</title>
<link rel="stylesheet" href="https://fonts.googleapis.com/css2?family=Questrial&family=Open+Sans:wght@400;600;700&display=swap">
<style>
  :root {
    --page: #e9e4dc;
    --card-night: #231a3d;
    --band-violet: #493b88;
    --bloom: #6a5f98;
    --paper-white: #ffffff;
    --ink-white: #ffffff;
    --ink-night: #1f1736;
  }
  * { box-sizing: border-box; margin: 0; padding: 0; }
  html, body {
    width: 1200px; height: 852px; overflow: hidden;
    background: var(--page);
  }
  .card {
    position: absolute; left: 80px; top: 129px;
    width: 1040px; height: 594px;
    border-radius: 28px; overflow: hidden;
    background: var(--card-night);
    box-shadow: 0 6px 18px rgba(0,0,0,.18);
    font-family: "Open Sans", sans-serif;
  }
  .name-band {
    position: absolute; left: 0; top: 88px;
    width: 590px; height: 166px;
    background: var(--band-violet);
  }
  .shop-name {
    position: absolute; left: 92px; top: 96px;
    font-family: "Questrial", sans-serif;
    font-weight: 400;
    font-size: 134px; line-height: 1; letter-spacing: 0;
    color: var(--ink-white);
    white-space: nowrap;
  }
  .tagline {
    position: absolute; left: 172px; top: 266px;
    font-size: 23px; line-height: 31px;
    color: var(--ink-white); text-transform: uppercase;
  }
  .phone-list {
    position: absolute; left: 192px; top: 336px;
    font-size: 22px; line-height: 40px; color: var(--ink-white);
    list-style: none;
  }
  .phone-list .label { display: inline-block; width: 100px; }
  .floral-motif {
    position: absolute; left: 640px; top: 20px;
    width: 330px; height: 390px;
    background: radial-gradient(ellipse at 45% 40%, var(--bloom) 0%, rgba(106,95,152,.55) 40%, rgba(35,26,61,0) 72%);
  }
  .contact-band {
    position: absolute; left: 0; bottom: 0;
    width: 100%; height: 160px;
    background: var(--paper-white);
  }
  .address {
    position: absolute; left: 196px; top: 24px;
    font-size: 24px; font-weight: 700; color: var(--ink-night);
    white-space: nowrap;
  }
  .email, .social {
    position: absolute; top: 76px;
    font-size: 24px; font-weight: 700; color: var(--ink-night);
    display: flex; align-items: center; gap: 14px;
    white-space: nowrap;
  }
  .email { left: 250px; }
  .social { left: 680px; }
  .social-square {
    width: 20px; height: 20px; background: var(--ink-night);
  }
</style>
</head>
<body>
  <div class="card">
    <div class="name-band"></div>
    <h1 class="shop-name">DELLA</h1>
    <p class="tagline">Retail high end contemporary<br>women's clothing store</p>
    <ul class="phone-list">
      <li><span class="label">Phone:</span>757.386.5049</li>
      <li><span class="label">Fax:</span>757.386-2613</li>
    </ul>
    <div class="floral-motif" role="img" aria-label="Decorative swirling flower ornament in soft violet"></div>
    <div class="contact-band">
      <p class="address">5417 Larkmoor Rd. #309 Ember Court Arcade, Va. Beach, Va. 23987</p>
      <p class="email">
        <svg width="26" height="20" viewBox="0 0 26 20" aria-hidden="true">
          <rect x="1.5" y="1.5" width="23" height="17" fill="none" stroke="#1f1736" stroke-width="2"/>
          <polyline points="1.5,1.5 13,11 24.5,1.5" fill="none" stroke="#1f1736" stroke-width="2"/>
        </svg>
        dellamode@quillbox.com
      </p>
      <p class="social"><span class="social-square"></span>MolvaHarbor</p>
    </div>
  </div>
</body>
</html>
```